TALLIS AT DWELLINGS, LLC Webpage portfolio

I want to create a Website that allows my potential clients to browse my Skilled work via before and after photos. I want the website to enhance the work that I provide and potentially drive new business, or at least solidify my work.
I also do 3D CAD and Modeling of New Spaces and it would be nice to show some of that work from pencil design to 3D modeling, which I feel may help give me more clients.

The website needs to show a solid carpenter/company with the skills to get any project completed.

Types of Jobs - Custom Carpentry & Finishes, Kitchens, Baths, Basements, Decks, Porches, Whole House Renovation - Skilled Craftsmanship (Hardwood Flooring, Floor and Wall Tile) and much more...

Target Market(s)

Residential Home Renovation, Kitchen and Bath Renovation, Home Improvement

Industry/Entity Type

Residential Construction

Number of Pages Required

5+ page

Font styles to use
Sans Serif
Script

Requirements
Must have
• Similar to Rimvale.com, except for Tallis At Dwellings.
• Must be inviting.
• My Services Offered
• A way to reach me or contact me for estimates with some sort of Screening Questionare.
Nice to have
• Inviting Colors
Should not have
• Not sure at this time

```html
<!DOCTYPE html>
<html lang="en">
<head>
<meta charset="utf-8">
<title>Tallis At Dwellings</title>
<link href="https://fonts.googleapis.com/css2?family=Questrial&display=swap" rel="stylesheet">
<style>
:root{
  --blue:#1a9ad6;
  --ink:#2f3a44;
  --text:#6b6b6b;
  --line:#e3e3e3;
  --footer:#4b4b4b;
  --footer-text:#c9c9c9;
  --white:#ffffff;
}
*{box-sizing:border-box;margin:0;padding:0}
html,body{width:1200px;height:3186px;overflow:hidden;background:var(--white)}
body{position:relative;font-family:'Questrial',Arial,sans-serif;color:var(--text)}
.abs{position:absolute}
a{color:inherit;text-decoration:none}

/* header */
.brand{left:159px;top:24px;display:flex;align-items:center;gap:10px}
.brand-mark{width:36px;height:36px;border-radius:50%;background:var(--blue)}
.brand-name{font-size:19px;color:#1c4f86;line-height:1}
.brand-tag{font-size:7px;color:#1c4f86;letter-spacing:.5px;margin-top:4px}
.nav{top:34px;font-size:14px;color:var(--ink)}
.nav.active{color:var(--blue)}
.nav.active::after{content:"";position:absolute;left:-4px;right:-4px;top:22px;height:2px;background:var(--blue)}
.btn-solid{background:var(--blue);color:var(--white);border-radius:20px;text-align:center;font-size:12px}
.btn-line{border:2px solid var(--blue);color:var(--blue);border-radius:20px;text-align:center;font-size:12px;background:var(--white)}

/* hero */
.hero{left:0;top:91px;width:1200px;height:400px;background:linear-gradient(160deg,#3c2a1e 0%,#6b4a33 40%,#8d7563 60%,#3a2b21 100%)}
.hero-title{left:0;width:1200px;top:118px;text-align:center;color:var(--white);font-size:38px;line-height:46px}
.hero-btn{left:535px;top:234px;width:128px;height:34px;line-height:30px;border:2px solid var(--white);color:var(--white);border-radius:20px;font-size:12px;text-align:center}

/* headings */
.section-title{left:0;width:1200px;text-align:center;font-size:27px;color:var(--ink)}
.section-title span,.accent{color:var(--blue)}
.title-rule{left:570px;width:60px;height:2px;background:var(--blue)}

/* about */
.about-title{left:155px;top:530px;font-size:27px;color:var(--ink)}
.about-rule{left:155px;top:578px;width:533px;height:1px;background:var(--line)}
.photo{display:block}
.about-sub{left:208px;top:770px;font-size:22px;color:var(--blue)}
.about-dash{left:159px;top:785px;width:32px;height:2px;background:var(--blue)}
.about-text{left:155px;top:810px;width:500px;font-size:12.5px;line-height:17.6px}

/* quote */
.quote{left:765px;top:540px;width:278px;height:441px;background:var(--white);box-shadow:0 2px 12px rgba(0,0,0,.15)}
.quote-head{height:89px;background:var(--blue);color:var(--white);text-align:center;padding-top:14px}
.quote-head h3{font-size:24px;font-weight:400}
.quote-head p{font-size:11px;line-height:15px;margin-top:4px}
.field{position:absolute;left:23px;width:232px;border:1px solid var(--line);font-size:11px;color:#aaa;padding:8px 10px}

/* service cards */
.card{background:var(--white);box-shadow:0 1px 8px rgba(0,0,0,.12)}
.card-label{position:absolute;left:0;right:0;top:140px;height:35px;line-height:35px;padding-left:24px;color:var(--white);font-size:15px;background:rgba(0,0,0,.35)}
.card-label.highlight{background:var(--blue)}
.card-text{position:absolute;left:24px;right:24px;top:191px;font-size:12px;line-height:16.5px}
.card-more{position:absolute;left:24px;top:286px;font-size:12px;color:var(--ink)}
.card-more.highlight{color:var(--blue);text-decoration:underline}

/* testimonial */
.testimonial{left:0;top:1514px;width:1200px;height:287px;background:linear-gradient(90deg,#5c6266,#8a8f92 50%,#5a5f62)}
.avatar{left:542px;top:1457px;width:114px;height:114px;border-radius:50%;background:linear-gradient(#c9c4bd,#8e8a86);border:5px solid var(--white)}
.testimonial-text{left:240px;top:1610px;width:720px;text-align:center;color:var(--white);font-size:13px;line-height:21px}
.testimonial-name{left:0;width:1200px;top:1716px;text-align:center;color:var(--white);font-size:18px}
.testimonial-role{left:0;width:1200px;top:1741px;text-align:center;color:#eee;font-size:11px}

/* work */
.work-frame{background:#dcdcdc;padding:13px}
.work-cap{position:absolute;bottom:13px;height:30px;line-height:30px;color:var(--white);font-size:13px;padding-left:12px;background:rgba(15,30,35,.85)}

/* blog */
.blog-date{position:absolute;left:50%;transform:translateX(-50%);top:181px;background:var(--blue);color:var(--white);font-size:11px;padding:3px 14px;white-space:nowrap}
.blog-title{position:absolute;left:20px;right:20px;top:220px;text-align:center;font-size:16px;line-height:20px;color:var(--ink)}
.blog-text{position:absolute;left:28px;right:28px;top:270px;text-align:center;font-size:12px;line-height:17px}
.blog-meta{position:absolute;left:24px;right:24px;top:375px;display:flex;justify-content:space-between;font-size:10px;color:#777}
.blog-rule{position:absolute;left:24px;right:24px;top:400px;height:1px;background:var(--line)}

/* footer */
.footer{left:0;top:2852px;width:1200px;height:275px;background:var(--footer)}
.foot-title{top:2896px;color:var(--white);font-size:17px}
.foot-text{color:var(--footer-text);font-size:11.5px;line-height:19px}
.foot-divider{top:2906px;width:1px;height:190px;background:#6a6a6a}
.social{top:3048px;width:28px;height:28px;border-radius:50%;border:2px solid var(--blue)}
.quick{left:915px;color:var(--footer-text);font-size:12px}
.quick.active{color:var(--blue)}
.copyright{left:155px;top:3148px;font-size:11px;color:#777}
</style>
</head>
<body>

<!-- header -->
<div class="abs brand">
  <div class="brand-mark"></div>
  <div>
    <div class="brand-name">Tallis At Dwellings</div>
    <div class="brand-tag">DESIGN BUILD &amp; REMODELING CONTRACTORS</div>
  </div>
</div>
<a class="abs nav active" style="left:357px">Home</a>
<a class="abs nav" style="left:440px">About Us</a>
<a class="abs nav" style="left:544px">Services</a>
<a class="abs nav" style="left:643px">Work</a>
<a class="abs nav" style="left:718px">Blog</a>
<a class="abs nav" style="left:789px">Contact Us</a>
<a class="abs btn-solid" style="left:915px;top:25px;width:128px;height:37px;line-height:37px">Free Estimate</a>

<!-- hero -->
<div class="abs hero" role="img" aria-label="Photo of a remodelled kitchen with granite countertops and sink"></div>
<div class="abs hero-title" style="top:209px">The New Way To Design<br>Your Home</div>
<a class="abs hero-btn" style="top:325px">Explore More</a>
<svg class="abs" style="left:108px;top:278px" width="26" height="24" viewBox="0 0 26 24"><path d="M10 2 2 10l8 8v-5c7 0 11 2 14 8-1-8-5-13-14-13V2z" fill="#fff"/></svg>
<svg class="abs" style="left:1066px;top:278px" width="26" height="24" viewBox="0 0 26 24"><path d="M16 2l8 8-8 8v-5C9 13 5 15 2 21c1-8 5-13 14-13V2z" fill="var(--blue)"/></svg>

<!-- about -->
<div class="abs about-title">Tallis <span class="accent">At</span> Dwellings</div>
<div class="abs about-rule"></div>
<div class="abs photo" style="left:155px;top:603px;width:531px;height:149px;background:linear-gradient(120deg,#d8d4cc,#c9b98e 45%,#e4e1da 70%,#b8b2a6)" role="img" aria-label="Model house resting on architectural plans and colour swatches"></div>
<div class="abs about-dash"></div>
<div class="abs about-sub">About Us</div>
<p class="abs about-text">There are many variations of passages of Lorem Ipsum available, but the majority have suffered alteration in some form, by injected humour, or randomised words which don't look even slightly believable. If you are going to use a passage of Lorem Ipsum, you need to be sure there isn't anything embarrassing hidden in the middle of text. All the Lorem Ipsum generators on the it is a long established fact that a reader.</p>
<a class="abs btn-solid" style="left:155px;top:945px;width:128px;height:34px;line-height:34px">Discover More</a>

<form class="abs quote">
  <div class="quote-head">
    <h3>Get A Quote</h3>
    <p>Enquire now and we call back<br>within 60 minutes!</p>
  </div>
  <div class="field" style="top:112px;height:32px">Name</div>
  <div class="field" style="top:157px;height:32px">Email</div>
  <div class="field" style="top:201px;height:32px">Phone</div>
  <div class="field" style="top:248px;height:115px">Message</div>
  <div class="abs btn-line" style="left:23px;top:375px;width:96px;height:32px;line-height:28px">&#10148; Send</div>
</form>

<!-- services -->
<h2 class="abs section-title" style="top:1018px"><span>Our</span> Services</h2>
<div class="abs title-rule" style="top:1058px"></div>

<div class="abs card" style="left:155px;top:1083px;width:280px;height:319px">
  <div style="height:177px;background:linear-gradient(135deg,#8c6a4e,#d9c9b4 55%,#5e4a3c)" role="img" aria-label="Renovated open living room and kitchen"></div>
  <div class="card-label">Home Renovation</div>
  <p class="card-text">Lorem Ipsum has been the industry's standard dummy text ever since the 1500s, when an unknown printer took galley of...</p>
  <a class="card-more">&bull; Read More</a>
</div>
<div class="abs card" style="left:459px;top:1083px;width:280px;height:319px">
  <div style="height:177px;background:linear-gradient(135deg,#d9d7d2,#f1efea 50%,#a9a39a)" role="img" aria-label="Bright renovated kitchen and bath"></div>
  <div class="card-label highlight">Kitchen and Bath Renovtion</div>
  <p class="card-text">Lorem Ipsum has been the industry's standard dummy text ever since the 1500s, when an unknown printer took galley of...</p>
  <a class="card-more highlight">&bull; Read More</a>
</div>
<div class="abs card" style="left:763px;top:1083px;width:280px;height:319px">
  <div style="height:177px;background:linear-gradient(135deg,#6f5d4c,#cfc6b8 50%,#8d7c68)" role="img" aria-label="Improved dining room with arched doorway"></div>
  <div class="card-label">Home Improvement</div>
  <p class="card-text">Lorem Ipsum has been the industry's standard dummy text ever since the 1500s, when an unknown printer took galley of...</p>
  <a class="card-more">&bull; Read More</a>
</div>

<!-- testimonial -->
<div class="abs testimonial" role="img" aria-label="Modern living room and kitchen interior, darkened"></div>
<div class="abs avatar" role="img" aria-label="Portrait of the client"></div>
<p class="abs testimonial-text">"Excellent service, quote given on the spot for major clean-up of household throw-outs. The team provides quick, efficient and courteous removal! Very satisfied customer."</p>
<svg class="abs" style="left:586px;top:1676px" width="28" height="26" viewBox="0 0 28 26"><circle cx="14" cy="13" r="12" fill="none" stroke="var(--blue)" stroke-width="2"/><path d="M8 15h4v4H8zM8 15c0-3 1-5 4-6M15 15h4v4h-4zM15 15c0-3 1-5 4-6" fill="none" stroke="var(--blue)" stroke-width="2"/></svg>
<div class="abs testimonial-name">Dale Harrow - Cedar Point</div>
<div class="abs testimonial-role">Residential Rubbish</div>
<svg class="abs" style="left:152px;top:1645px" width="26" height="24" viewBox="0 0 26 24"><path d="M10 2 2 10l8 8v-5c7 0 11 2 14 8-1-8-5-13-14-13V2z" fill="#fff"/></svg>
<svg class="abs" style="left:1022px;top:1645px" width="26" height="24" viewBox="0 0 26 24"><path d="M16 2l8 8-8 8v-5C9 13 5 15 2 21c1-8 5-13 14-13V2z" fill="var(--blue)"/></svg>

<!-- work -->
<h2 class="abs section-title" style="top:1840px"><span>Our</span> Work</h2>
<div class="abs title-rule" style="top:1880px"></div>

<div class="abs work-frame" style="left:232px;top:1907px;width:365px;height:238px">
  <div style="display:flex;height:212px;gap:2px">
    <div style="flex:1;background:linear-gradient(150deg,#c9a36a,#6e4a2c)" role="img" aria-label="Living room before renovation"></div>
    <div style="flex:1;background:linear-gradient(150deg,#e0c79c,#8a5a34)" role="img" aria-label="Living room after renovation"></div>
  </div>
  <div class="work-cap" style="left:13px;width:169px">Before</div>
  <div class="work-cap" style="left:184px;width:168px">After</div>
</div>
<svg class="abs" style="left:397px;top:2009px" width="32" height="32" viewBox="0 0 32 32"><circle cx="16" cy="16" r="16" fill="var(--blue)"/><path d="M9 16l5 5 9-10" fill="none" stroke="#fff" stroke-width="2.5"/></svg>

<div class="abs work-frame" style="left:612px;top:1907px;width:357px;height:238px">
  <div style="display:flex;height:212px;gap:2px">
    <div style="flex:1;background:linear-gradient(170deg,#9fb1bf,#c7b8b0 55%,#e7e6e2)" role="img" aria-label="House exterior before renovation"></div>
    <div style="flex:1;background:linear-gradient(170deg,#7f9a6a,#7d7f84 55%,#5c6b4a)" role="img" aria-label="House exterior after renovation"></div>
  </div>
  <div class="work-cap" style="left:13px;width:165px">Before</div>
  <div class="work-cap" style="left:180px;width:164px">After</div>
</div>
<svg class="abs" style="left:152px;top:2014px" width="26" height="24" viewBox="0 0 26 24"><path d="M10 2 2 10l8 8v-5c7 0 11 2 14 8-1-8-5-13-14-13V2z" fill="#aaa"/></svg>
<svg class="abs" style="left:1022px;top:2014px" width="26" height="24" viewBox="0 0 26 24"><path d="M16 2l8 8-8 8v-5C9 13 5 15 2 21c1-8 5-13 14-13V2z" fill="var(--blue)"/></svg>
<a class="abs btn-line" style="left:552px;top:2179px;width:96px;height:32px;line-height:28px">View All</a>

<!-- blog -->
<h2 class="abs section-title" style="top:2248px"><span>Our</span> Latest Blog</h2>
<div class="abs title-rule" style="top:2288px"></div>

<article class="abs" style="left:155px;top:2315px;width:280px;height:489px;border:1px solid #eee">
  <div style="margin:23px 24px 0;height:158px;background:linear-gradient(160deg,#8c9aa5,#e2e0da 50%,#7a7262)" role="img" aria-label="Renovated front porch"></div>
  <div class="blog-date">25 Oct, 2016</div>
  <h3 class="blog-title" style="font-weight:400">The standard Lorem<br>Ipsum passage</h3>
  <p class="blog-text">There are many variations of passages of Lorem Ipsum available, but the majority have suffered alteration in some form.</p>
  <div class="blog-meta"><span>&#9823; Lorem</span><span>&#9633; 30 Comment</span><span>&lt; Share</span></div>
  <div class="blog-rule"></div>
  <a class="abs btn-line" style="left:92px;top:434px;width:96px;height:32px;line-height:28px">Read More</a>
</article>
<article class="abs" style="left:459px;top:2315px;width:280px;height:489px;box-shadow:0 2px 12px rgba(0,0,0,.15)">
  <div style="margin:23px 24px 0;height:158px;background:linear-gradient(160deg,#3a2618,#a06a3c 50%,#4a3020)" role="img" aria-label="Kitchen with wood cabinets and pendant lights"></div>
  <div class="blog-date">30 Oct, 2016</div>
  <h3 class="blog-title" style="font-weight:400">The standard Lorem<br>Ipsum passage</h3>
  <p class="blog-text">There are many variations of passages of Lorem Ipsum available, but the majority have suffered alteration in some form.</p>
  <div class="blog-meta"><span>&#9823; Lorem</span><span>&#9633; 30 Comment</span><span>&lt; Share</span></div>
  <div class="blog-rule"></div>
  <a class="abs btn-solid" style="left:92px;top:434px;width:96px;height:32px;line-height:32px">Read More</a>
</article>
<article class="abs" style="left:763px;top:2315px;width:280px;height:489px;border:1px solid #eee">
  <div style="margin:23px 24px 0;height:158px;background:linear-gradient(160deg,#5a3a26,#b58a5a 50%,#6a4430)" role="img" aria-label="Dining room with wood floors"></div>
  <div class="blog-date">05 Jan, 2016</div>
  <h3 class="blog-title" style="font-weight:400">The standard Lorem<br>Ipsum passage</h3>
  <p class="blog-text">There are many variations of passages of Lorem Ipsum available, but the majority have suffered alteration in some form.</p>
  <div class="blog-meta"><span>&#9823; Lorem</span><span>&#9633; 30 Comment</span><span>&lt; Share</span></div>
  <div class="blog-rule"></div>
  <a class="abs btn-line" style="left:92px;top:434px;width:96px;height:32px;line-height:28px">Read More</a>
</article>

<!-- footer -->
<footer class="abs footer"></footer>
<div class="abs foot-title" style="left:155px">Tallis At Dwellings</div>
<p class="abs foot-text" style="left:155px;top:2936px">Maple Ridge, WA<br>Sed ut perspiciatis unde omnis 3456123</p>
<div class="abs" style="left:155px;top:2986px;color:#fff;font-size:18px">Call Us <span style="color:var(--blue)">&#9742;</span> 0412 555 018</div>
<div class="abs foot-text" style="left:155px;top:3012px">info@tallisatdwellings.com</div>
<div class="abs social" style="left:155px"></div>
<div class="abs social" style="left:192px"></div>
<div class="abs social" style="left:229px"></div>
<div class="abs social" style="left:266px"></div>

<div class="abs foot-divider" style="left:484px"></div>
<div class="abs foot-title" style="left:535px">Newsletter</div>
<p class="abs foot-text" style="left:535px;top:2936px;width:270px">Subscribe to our Newsletter to get the latest scoop right to your inbox</p>
<div class="abs" style="left:535px;top:2990px;width:280px;height:32px;background:#5c5c5c;color:#ccc;font-size:11px;line-height:32px;padding-left:12px">Enter your email...</div>
<div class="abs" style="left:535px;top:3048px;width:96px;height:30px;border:2px solid var(--blue);border-radius:20px;color:var(--blue);font-size:12px;text-align:center;line-height:26px">&#10148; Send</div>

<div class="abs foot-divider" style="left:860px"></div>
<div class="abs foot-title" style="left:915px">Quick Link</div>
<a class="abs quick active" style="top:2936px">&rsaquo; Home</a>
<a class="abs quick" style="top:2963px">&rsaquo; About</a>
<a class="abs quick" style="top:2993px">&rsaquo; Services</a>
<a class="abs quick" style="top:3023px">&rsaquo; Work</a>
<a class="abs quick" style="top:3051px">&rsaquo; Contact</a>

<div class="abs copyright">&copy; 2017 Tallis At Dwellings. All rights reserved.</div>
<svg class="abs" style="left:1024px;top:3144px" width="20" height="22" viewBox="0 0 20 22"><path d="M10 2 2 11h5v9h6v-9h5z" fill="var(--blue)"/></svg>

</body>
</html>
```